Business Cards Design for the electrical wholesaler: clean bold dynamic :)

We need a business card design that would follow our latest brand guidelines. As an electrical wholesaler we want to bring a fresh look and feel into the industry. The design should be clean bold and dynamic. It should come alive with the renewed energy of our green colour. Our grey colour should keep things balanced and complement the notion of maturity and responsibility. We employ Lato as a corporate font however are not bound by this font and we’re open to interpretation here.

Target Market(s)

Electrical contractors

Industry/Entity Type

Business

Contact Information for Business Card

Logo
Name & Surname: Olesia Hrybenko
Job Title: Director of Marketing
Email: olesia.hrybenko@mailvex.com
Cell phone: XXX.XXX.XXXX
Address: 20517 - 88 Ave. Edmonton, AB, Canada. T6K 2N8
Business Phone: 780.362.7048
Website: www.kopra.ca

Font styles to use
Other font styles liked:
• Lato

Requirements
Must have
• Logo & website
Nice to have
• Brand elements - some of them you may find in the attached Brand Guidelines (e.g. three lines on the background signifying "W")

```html
<!DOCTYPE html>
<html lang="en">
<head>
<meta charset="utf-8">
<title>Kopra Electrical Wholesalers – Business Card</title>
<link rel="stylesheet" href="https://fonts.googleapis.com/css2?family=Oswald:wght@600&family=Work+Sans:wght@400;500&display=swap">
<style>
  :root {
    --bg: #111213;
    --card: #1f2021;
    --card-edge: #2a2b2c;
    --green: #86c540;
    --white: #f4f4f4;
    --muted: #d9d9d9;
  }
  * { box-sizing: border-box; margin: 0; padding: 0; }
  html, body {
    width: 1200px; height: 900px; overflow: hidden;
    background: var(--bg);
  }
  .stage {
    width: 1200px; height: 900px;
    display: flex; flex-direction: column; align-items: center; justify-content: center;
    gap: 44px;
    font-family: "Work Sans", sans-serif;
  }
  .card {
    position: relative;
    width: 640px; height: 366px;
    background: linear-gradient(135deg, var(--card) 0%, var(--card) 55%, var(--card-edge) 100%);
    border-bottom: 4px solid var(--green);
  }

  /* Front */
  .brand {
    position: absolute; left: 0; right: 0; top: 128px;
    display: flex; flex-direction: column; align-items: center;
  }
  .brand-row { display: flex; align-items: center; gap: 16px; }
  .brand-dot { width: 40px; height: 40px; border-radius: 50%; background: var(--green); }
  .brand-name {
    font-weight: 500; font-size: 64px; line-height: 1; color: var(--white);
    letter-spacing: 1px;
  }
  .brand-tagline {
    margin-top: 10px; margin-left: 56px;
    font-weight: 500; font-size: 11px; letter-spacing: 2.6px; color: var(--white);
    text-transform: uppercase;
  }

  /* Back */
  .identity {
    position: absolute; right: 358px; top: 112px; text-align: right;
  }
  .person-name {
    font-family: "Oswald", sans-serif; font-weight: 600;
    font-size: 36px; line-height: 1; color: var(--green);
    text-transform: uppercase; letter-spacing: 0.5px;
  }
  .person-role {
    margin-top: 6px;
    font-size: 17px; color: var(--white); letter-spacing: 1px;
  }
  .divider {
    position: absolute; left: 302px; top: 118px;
    width: 2px; height: 70px; background: var(--green);
  }
  .contacts {
    position: absolute; left: 322px; top: 116px;
    list-style: none;
  }
  .contacts li {
    display: flex; align-items: center; gap: 12px;
    font-size: 17px; color: var(--white); letter-spacing: 1px;
    height: 25px;
  }
  .contacts svg { width: 12px; height: 12px; flex: none; }
  .accent { color: var(--green); }
  .address {
    position: absolute; left: 84px; bottom: 54px;
    font-size: 17px; color: var(--white); letter-spacing: 1.2px;
  }
</style>
</head>
<body>
<main class="stage">
  <section class="card card-front">
    <div class="brand">
      <div class="brand-row">
        <span class="brand-dot"></span>
        <span class="brand-name">kopra</span>
      </div>
      <span class="brand-tagline">Electrical Wholesalers</span>
    </div>
  </section>

  <section class="card card-back">
    <div class="identity">
      <h1 class="person-name">Olesia Hrybenko</h1>
      <p class="person-role">Founder</p>
    </div>
    <span class="divider"></span>
    <ul class="contacts">
      <li>
        <svg viewBox="0 0 12 12" aria-hidden="true"><path d="M3 1 L5 3.5 L4 5 Q5.5 7.5 7 8 L8.5 7 L11 9 L9.5 11 Q5 10.5 1.5 5 Q1 2.5 3 1Z" fill="none" stroke="#86c540" stroke-width="1"/></svg>
        <span>780.362.7048</span>
      </li>
      <li>
        <svg viewBox="0 0 12 12" aria-hidden="true"><rect x="1" y="2.5" width="10" height="7" fill="none" stroke="#86c540" stroke-width="1"/><path d="M1 2.5 L6 6.5 L11 2.5" fill="none" stroke="#86c540" stroke-width="1"/></svg>
        <span>hello@kopra.ca</span>
      </li>
      <li>
        <svg viewBox="0 0 12 12" aria-hidden="true"><circle cx="6" cy="6" r="5" fill="none" stroke="#86c540" stroke-width="1"/><ellipse cx="6" cy="6" rx="2.2" ry="5" fill="none" stroke="#86c540" stroke-width="1"/><path d="M1 6 H11" stroke="#86c540" stroke-width="1"/></svg>
        <span>www.<span class="accent">kopra</span>.ca</span>
      </li>
    </ul>
    <p class="address">20517 88ave T6K2N8 Edmonton, Alberta</p>
  </section>
</main>
</body>
</html>
```